Business incubator; Angel investments; Consulting for startups

We need new office equipment

Target Market(s)

Start up Company

Font styles to use
Sans Serif

Colors

Designer to choose only greyscale colors for use in the design.

Requirements
Must have
• Existing company logo
Nice to have
• Corporate according to the website www.tmv-norlix.com
Should not have
• Colors off gray

```html
<!DOCTYPE html>
<html lang="en">
<head>
<meta charset="utf-8">
<title>TMV Norlix Letterhead</title>
<link href="https://fonts.googleapis.com/css2?family=Montserrat:wght@400;500;600&family=Poppins:wght@300;400;500&display=swap" rel="stylesheet">
<style>
  :root{
    --backdrop:#e6e7e8;
    --paper:#ffffff;
    --logo-grey:#6d6e70;
    --band-grey:#d2d3d5;
    --icon-grey:#a7a8aa;
    --ink:#2b2b2b;
    --ink-mid:#555657;
    --ink-soft:#7a7b7d;
    --ink-faint:#a3a4a6;
  }
  *{margin:0;padding:0;box-sizing:border-box;}
  html,body{width:1096px;height:1200px;overflow:hidden;background:var(--backdrop);}
  body{font-family:"Poppins",sans-serif;color:var(--ink);position:relative;}
  .letterhead{position:absolute;left:108px;top:24px;width:880px;height:1152px;background:var(--paper);box-shadow:0 4px 18px rgba(0,0,0,.12);overflow:hidden;}
  .brand-block{position:absolute;left:28px;top:16px;width:136px;height:136px;background:var(--logo-grey);display:flex;align-items:center;justify-content:center;color:#fff;font-family:"Poppins",sans-serif;font-weight:500;font-size:28px;letter-spacing:1px;}
  .header-rule{position:absolute;left:192px;top:137px;width:688px;height:15px;background:var(--band-grey);}
  .recipient{position:absolute;left:32px;top:227px;font-family:"Montserrat",sans-serif;}
  .recipient .label{font-size:14px;color:var(--ink);line-height:20px;}
  .recipient .name{font-size:18px;font-weight:600;letter-spacing:1px;line-height:22px;margin-top:0;}
  .recipient .role{font-size:14px;color:var(--ink-mid);line-height:22px;}
  .recipient .contact{font-size:14px;color:var(--ink-soft);line-height:20.5px;margin-top:7px;}
  .recipient .contact.address{color:var(--ink);font-weight:600;}
  .date{position:absolute;right:51px;top:302px;font-family:"Montserrat",sans-serif;font-size:14px;color:var(--ink-mid);}
  .date strong{color:var(--ink);font-weight:600;}
  .body-copy{position:absolute;left:32px;top:412px;width:810px;font-size:14.3px;line-height:23.5px;color:var(--ink);text-align:justify;font-weight:400;}
  .body-copy p+p{margin-top:23.5px;}
  .signature-mark{position:absolute;left:8px;top:809px;width:218px;height:42px;background:linear-gradient(90deg,#f1f1f2,#e3e4e5,#f1f1f2);border-radius:4px;}
  .signatory{position:absolute;left:32px;top:857px;font-family:"Poppins",sans-serif;}
  .signatory .name{font-size:17.5px;font-weight:500;letter-spacing:.6px;line-height:24px;}
  .signatory .title{font-size:14px;color:var(--ink-faint);letter-spacing:1.2px;line-height:22px;}
  .contact-strip{position:absolute;top:998px;left:0;width:880px;height:37px;}
  .contact-item{position:absolute;top:0;display:flex;align-items:center;gap:12px;}
  .contact-icon{width:37px;height:37px;background:var(--icon-grey);border-radius:4px;display:flex;align-items:center;justify-content:center;flex-shrink:0;}
  .contact-icon svg{width:18px;height:18px;fill:#fff;}
  .contact-text{font-size:12px;line-height:17px;color:var(--ink-soft);font-weight:300;}
  .contact-item.address{left:62px;}
  .contact-item.email{left:347px;}
  .contact-item.web{left:631px;}
  .footer-band{position:absolute;left:0;top:1066px;width:880px;height:86px;}
  .footer-band svg{position:absolute;inset:0;}
  .footer-name{position:absolute;left:0;width:880px;top:10px;text-align:center;font-size:19px;color:var(--logo-grey);font-weight:400;}
</style>
</head>
<body>
<main class="letterhead">
  <div class="brand-block">TMV</div>
  <div class="header-rule"></div>

  <section class="recipient">
    <div class="label">To</div>
    <div class="name">Ravi Menon</div>
    <div class="role">CEO, BRIGHTLANE STUDIO</div>
    <div class="contact">P: +91 90210 4567, +91 80345 11290</div>
    <div class="contact" style="margin-top:0">W: hello@brightlane.com, www.brightlane.com</div>
    <div class="contact address" style="margin-top:0">A: 45 Lake View Road, Pune, India 411001</div>
  </section>

  <div class="date"><strong>Date:</strong> 24-03-2018</div>

  <section class="body-copy">
    <p>Lorem ipsum dolor sit amet, consectetur adipiscing elit. Pellentesque dictum, ante non ullamcorp er convallis, nunc quam blandit metus, ac mollis eros felis a orci. Donec congue, mauris ut pulvinar lobortis, dolor massa feugiat nisi, at tincidunt metus leo vel elit. Proin facilisis semper lobortis. Vivamus augue purus, cursus quis urna non, accumsan pellentesque est. Nulla in iaculis magna, quis aliqu et ex. Cras efficitur metus eget purus euismod facilisis. Proin non metus tincidunt, auctor ipsum a, tempor mi.</p>
    <p>Nulla egestas vulputate risus, ut vestibulum diam commodo id. Mauris ornare libero eu erat portt itor ultrices. Proin sed lectus scelerisque ligula bibendum sagittis ac nec leo. Donec ac accumsan diam, et lobortis mauris.</p>
    <p>Nulla congue volutpat nisl ac lobortis. Integer dignissim interdum libero, quis feugiat velit pretium at. Phasellus sit amet libero rutrum, feugiat odio et, tempus purus.</p>
    <p>Nulla congue volutpat nisl ac lobortis. Integer dignissim interdum libero, quis feugiat velit pretium at. Phasellus sit amet libero rutrum, feugiat odio et, tempus purus. Cras ultricies.</p>
  </section>

  <div class="signature-mark" role="img" aria-label="Handwritten signature of the chairman"></div>
  <section class="signatory">
    <div class="name">ELLA MARSH</div>
    <div class="title">Chairman</div>
  </section>

  <section class="contact-strip">
    <div class="contact-item address">
      <span class="contact-icon"><svg viewBox="0 0 24 24"><path d="M12 2C8.1 2 5 5.1 5 9c0 5.2 7 13 7 13s7-7.8 7-13c0-3.9-3.1-7-7-7zm0 9.5A2.5 2.5 0 1 1 12 6.5a2.5 2.5 0 0 1 0 5z"/></svg></span>
      <span class="contact-text">4th Floor, 18 Harbour Lane,<br>London E1 7QX, United Kingdom</span>
    </div>
    <div class="contact-item email">
      <span class="contact-icon"><svg viewBox="0 0 24 24"><path d="M3 5h18v2l-9 6-9-6V5zm0 4.4l9 6 9-6V19H3V9.4z"/></svg></span>
      <span class="contact-text">info@tmv-norlix.com</span>
    </div>
    <div class="contact-item web">
      <span class="contact-icon"><svg viewBox="0 0 24 24"><path d="M12 2C8.1 2 5 5.1 5 9c0 5.2 7 13 7 13s7-7.8 7-13c0-3.9-3.1-7-7-7zm0 9.5A2.5 2.5 0 1 1 12 6.5a2.5 2.5 0 0 1 0 5z"/></svg></span>
      <span class="contact-text">www.tmv-norlix.com</span>
    </div>
  </section>

  <footer class="footer-band">
    <svg viewBox="0 0 880 86" width="880" height="86" aria-hidden="true">
      <rect x="0" y="0" width="880" height="86" fill="var(--band-grey)"/>
      <path d="M290,0 C304,0 308,5 312,15 L322,36 C326,43 331,45 340,45 L532,45 C541,45 546,42 550,35 L560,15 C565,4 570,0 584,0 Z" fill="var(--paper)"/>
    </svg>
    <div class="footer-name">TMV NORLIX PLC</div>
  </footer>
</main>
</body>
</html>
```